Doctor in Veterinary Medecine/ veterinarian

I am a vet and would like a buisness card which is simple yet elegant and professional.
My aim is to help as much animals as I can. My main field of expertise are dogs and cats. I would like the card to reflect a "family doctor" feeling.
It should not be the traditional picture of a paw or a dog but yet it should have a sign of a pet on it. I would like to have my name Lina Haddour as well as my profession D.V.M and my number.

Target Market(s)

Lebanese population who have pets

Industry/Entity Type

Doctor

Contact Information for Business Card

Should contain my profession " D.V.M", my full name "Lina Haddour" and my number "0096171552934"

Requirements
Must have
• A certain picture depicting my profession
Nice to have
• Some sort of picture related to pets and animals
Should not have
• A picture of a paw or a dog. I need something more creative

```html
<!DOCTYPE html>
<html lang="en">
<head>
<meta charset="utf-8">
<title>Dr. Lina Haddour – D.V.M Business Card</title>
<link rel="stylesheet" href="https://fonts.googleapis.com/css2?family=Tinos:wght@400;700&family=Arimo:wght@400&display=swap">
<style>
  :root {
    --bg: #e9e6e1;
    --card: #f7f7f7;
    --orange: #ef8436;
    --magenta: #bd5e8b;
    --teal: #267a98;
    --blue: #00a0d6;
    --name: #217c99;
    --ink: #111111;
    --icon-tint: rgba(255, 255, 255, 0.28);
  }
  * { margin: 0; padding: 0; box-sizing: border-box; }
  html, body {
    width: 1200px;
    height: 960px;
    overflow: hidden;
    background: var(--bg);
  }
  .canvas {
    position: relative;
    width: 1200px;
    height: 960px;
    display: flex;
    align-items: center;
    justify-content: center;
  }
  .business-card {
    position: relative;
    width: 1000px;
    height: 572px;
    background: var(--card);
    border-radius: 30px;
    overflow: hidden;
    box-shadow: 0 10px 30px rgba(0, 0, 0, 0.15);
  }
  .band { position: absolute; }
  .band--orange {
    left: 0; top: 118px; width: 448px; height: 146px;
    background: var(--orange);
    border-top-right-radius: 26px;
  }
  .band--blue {
    left: 0; top: 272px; width: 470px; height: 100px;
    background: var(--blue);
    border-bottom-right-radius: 26px;
  }
  .band--magenta {
    left: 458px; top: 22px; width: 542px; height: 142px;
    background: var(--magenta);
    border-top-left-radius: 26px;
  }
  .band--teal {
    left: 478px; top: 172px; width: 522px; height: 200px;
    background: var(--teal);
    border-bottom-left-radius: 26px;
  }
  .pet-icon {
    position: absolute;
    width: 112px;
    height: 112px;
    border-radius: 12px;
    background: var(--icon-tint);
  }
  .pet-icon--rabbit { left: 322px; top: 136px; }
  .pet-icon--cat    { left: 488px; top: 38px; }
  .pet-icon--dog    { left: 340px; top: 266px; width: 116px; height: 96px; }
  .pet-icon--bird   { left: 500px; top: 232px; }

  .identity {
    position: absolute;
    left: 190px;
    top: 420px;
    text-align: center;
  }
  .identity__name {
    font-family: "Tinos", "Times New Roman", serif;
    font-weight: 700;
    font-size: 52px;
    color: var(--name);
    letter-spacing: -0.5px;
    line-height: 1;
  }
  .identity__title {
    font-family: "Arimo", Arial, sans-serif;
    font-size: 30px;
    color: var(--ink);
    margin-top: 8px;
    letter-spacing: 1px;
  }
  .divider {
    position: absolute;
    left: 616px;
    top: 388px;
    width: 2px;
    height: 138px;
    background: var(--ink);
  }
  .contact__phone {
    position: absolute;
    left: 664px;
    top: 404px;
    font-family: "Arimo", Arial, sans-serif;
    font-size: 27px;
    color: var(--ink);
    letter-spacing: 0.5px;
  }
</style>
</head>
<body>
  <main class="canvas">
    <article class="business-card">
      <div class="band band--orange"></div>
      <div class="band band--blue"></div>
      <div class="band band--magenta"></div>
      <div class="band band--teal"></div>

      <div class="pet-icon pet-icon--rabbit" role="img" aria-label="White rabbit silhouette icon"></div>
      <div class="pet-icon pet-icon--cat" role="img" aria-label="White cat head icon"></div>
      <div class="pet-icon pet-icon--dog" role="img" aria-label="White dog head silhouette icon"></div>
      <div class="pet-icon pet-icon--bird" role="img" aria-label="White bird silhouette icon"></div>

      <div class="identity">
        <h1 class="identity__name">Dr.Lina Haddour</h1>
        <p class="identity__title">D.V.M</p>
      </div>

      <div class="divider"></div>

      <p class="contact__phone">0096171552934</p>
    </article>
  </main>
</body>
</html>
```